Bright-loop stitchworks Business Card

embroidery printing

Target Market(s)

Businesses and public

Industry/Entity Type

Business

Contact Information for Business Card

Front of card..... Bright-loop stitchworks .... Dorian Felkway..... 868 512-7743.... Email... bright_loopstitchworks@mailvane.net

Back of card..... Bright-loop stitchworks embroidery & artwork

Colors
000000

```html
<!DOCTYPE html>
<html lang="en">
<head>
<meta charset="utf-8">
<title>Bright-loop stitchworks Business Card</title>
<link href="https://fonts.googleapis.com/css2?family=Roboto:wght@400;700&family=Tinos&display=swap" rel="stylesheet">
<style>
  :root {
    --page: #e9e6e2;
    --card-white: #ffffff;
    --maroon: #7a1517;
    --accent-orange: #d9862b;
    --accent-grey: #a9a8aa;
    --brand-red: #e0342f;
    --ink: #1a1a1a;
    --ink-soft: #4a4a4a;
    --card-black: #0b0b0b;
    --on-dark: #f2f2f2;
  }
  * { box-sizing: border-box; margin: 0; padding: 0; }
  html, body { width: 1200px; height: 892px; overflow: hidden; }
  body {
    background: var(--page);
    font-family: "Roboto", Arial, sans-serif;
    position: relative;
  }
  .card {
    position: absolute;
    width: 540px;
    height: 309px;
    border-radius: 4px;
    overflow: hidden;
    box-shadow: 0 6px 18px rgba(0,0,0,0.18);
  }
  .card--front { left: 40px; top: 292px; background: var(--card-white); }
  .card--back { left: 620px; top: 292px; background: var(--card-black); }

  .front-curve { position: absolute; inset: 0; width: 100%; height: 100%; }

  .brand-name {
    position: absolute;
    font-family: "Roboto", Arial, sans-serif;
    font-weight: 700;
    line-height: 1;
    text-transform: uppercase;
    letter-spacing: 1px;
  }
  .card--front .brand-name { left: 34px; top: 34px; color: var(--ink-soft); font-size: 30px; }
  .brand-name span { display: block; }
  .brand-name .brand-sub { font-size: 22px; letter-spacing: 5px; margin-top: 6px; }

  .person { position: absolute; left: 300px; top: 40px; }
  .person-name { font-family: "Tinos", "Times New Roman", serif; color: var(--brand-red); font-size: 27px; }
  .person-role { color: var(--ink); font-size: 15px; margin-top: 2px; }

  .contact-list { position: absolute; right: 24px; top: 126px; list-style: none; text-align: right; }
  .contact-list li {
    display: flex; justify-content: flex-end; align-items: center; gap: 8px;
    font-size: 12px; color: var(--ink); margin-bottom: 9px;
  }
  .contact-icon { width: 12px; height: 12px; background: var(--brand-red); border-radius: 2px; flex: none; }

  .address {
    position: absolute; left: 30px; bottom: 26px;
    display: flex; gap: 8px; align-items: flex-start;
    color: var(--on-dark); font-size: 13px; line-height: 1.35;
  }
  .address svg { margin-top: 2px; flex: none; }

  .card--back .brand-name {
    left: 0; right: 0; top: 82px; text-align: center;
    color: var(--brand-red); font-size: 34px;
  }
  .card--back .brand-name .brand-sub { font-size: 24px; letter-spacing: 7px; margin-top: 8px; }
  .back-web {
    position: absolute; left: 40px; right: 40px; top: 205px;
    display: flex; align-items: center; gap: 14px;
    color: var(--on-dark); font-size: 17px; letter-spacing: 0.5px;
  }
  .back-web .rule { flex: 1; height: 1px; background: var(--on-dark); }
</style>
</head>
<body>
  <section class="card card--front" aria-label="Card front">
    <svg class="front-curve" viewBox="0 0 540 309" preserveAspectRatio="none" aria-hidden="true">
      <path d="M0,118 C70,250 280,292 540,286 L540,309 L0,309 Z" fill="var(--accent-grey)"/>
      <path d="M0,128 C72,256 280,298 540,293 L540,309 L0,309 Z" fill="var(--accent-orange)"/>
      <path d="M0,140 C75,262 280,304 540,300 L540,309 L0,309 Z" fill="var(--maroon)"/>
    </svg>

    <div class="brand-name"><span>Bright-loop</span><span class="brand-sub">stitchworks</span></div>

    <div class="person">
      <p class="person-name">Dorian Felkway</p>
      <p class="person-role">Managing Director</p>
    </div>

    <ul class="contact-list">
      <li>868 512-7743 <span class="contact-icon"></span></li>
      <li>www.brightloopstitch.com <span class="contact-icon"></span></li>
      <li>bright_loopstitchworks@mailvane.net <span class="contact-icon"></span></li>
    </ul>

    <div class="address">
      <svg width="11" height="14" viewBox="0 0 11 14" aria-hidden="true">
        <path d="M5.5 0C2.5 0 0 2.3 0 5.3 0 9 5.5 14 5.5 14S11 9 11 5.3C11 2.3 8.5 0 5.5 0Z" fill="var(--on-dark)"/>
        <circle cx="5.5" cy="5.2" r="2" fill="var(--maroon)"/>
      </svg>
      <p>Wexmoor Lane, London<br>United Kingdom</p>
    </div>
  </section>

  <section class="card card--back" aria-label="Card back">
    <div class="brand-name"><span>Bright-loop</span><span class="brand-sub">stitchworks</span></div>
    <div class="back-web"><span class="rule"></span>www.brightloopstitch.com<span class="rule"></span></div>
  </section>
</body>
</html>
```